Simple Slide from Excel on History of Technology

I need to convert this timeline into a more readable and friendly slide for a report I am doing. It is in Excel format. Feel free to cut some of the words and make it more simple. It can be in Word, powerpoint or excel.

Target Market(s)

a school paper, a professor will see

Requirements
Must have
• should give a feeling of momentum over time. Please add the number of internet users for each year it is available as 1,000 in 1975, 30,000 in 1987, 14 million in 1993, 25 million in 1994, 45 million in 1995, 77 million in 1996, 121 million in 1997, 188 million in 1998, 281 million in 1999, 413 million in 2000, 910 million in 2004, 1.4 billion in 2007

```html
<!DOCTYPE html>
<html lang="en">
<head>
<meta charset="utf-8">
<title>History of the Internet Timeline</title>
<link rel="stylesheet" href="https://fonts.googleapis.com/css2?family=Lato:ital,wght@0,400;0,700;1,400&display=swap">
<style>
  :root {
    --bg: #2a2a2a;
    --text: #e8e8e8;
    --muted: #bdbdbd;
    --area: #4a4a4a;
    --axis: #ffffff;
    --blue: #4f81bd;
    --red: #d0413e;
    --green: #9bbb59;
    --purple: #8f72b4;
    --teal: #4bacc6;
  }
  html, body { margin: 0; padding: 0; overflow: hidden; background: var(--bg); }
  .slide {
    position: relative; width: 1200px; height: 900px; overflow: hidden;
    background: var(--bg); color: var(--text);
    font-family: "Lato", sans-serif;
  }
  .graphics { position: absolute; left: 0; top: 0; width: 1200px; height: 900px; }
  .event { position: absolute; white-space: nowrap; }
  .event h3 { margin: 0; font-size: 19px; font-weight: 400; line-height: 22px; }
  .event p { margin: 0; font-size: 13px; line-height: 17px; }
  .sixties h3 { color: var(--blue); }
  .seventies h3 { color: var(--red); }
  .eighties h3 { color: var(--green); }
  .nineties h3 { color: var(--purple); }
  .noughties h3 { color: var(--teal); }
  .decade { position: absolute; font-size: 29px; font-weight: 700; line-height: 1; }
  .decade.sixties { color: var(--blue); }
  .decade.seventies { color: var(--red); }
  .decade.eighties { color: var(--green); }
  .decade.nineties { color: var(--purple); }
  .decade.noughties { color: var(--teal); }
  .users { position: absolute; text-align: center; line-height: 15px; white-space: nowrap; }
  .users b { display: block; font-size: 15px; font-weight: 700; }
  .users span { display: block; font-size: 12.5px; color: var(--text); }
  .users.red b { color: var(--red); }
  .users.green b { color: var(--green); }
  .users.purple b { color: var(--purple); }
  .users.teal b { color: var(--teal); }
  .chart-title { position: absolute; left: 848px; top: 310px; font-size: 18px; font-weight: 700; color: var(--muted); letter-spacing: 0.3px; }
</style>
</head>
<body>
<div class="slide">
  <svg class="graphics" viewBox="0 0 960 720" aria-hidden="true">
    <polygon fill="var(--area)" points="200,330 222,314 396,295 500,262 543,242 590,220 632,182 674,145 716,115 764,90 826,76 870,50 909,27 912,27 912,358 200,358"/>
    <!-- connectors -->
    <g stroke-width="1">
      <line x1="79" y1="358" x2="79" y2="262" stroke="var(--blue)"/>
      <line x1="48" y1="262" x2="110" y2="262" stroke="var(--blue)"/>
      <line x1="155" y1="358" x2="155" y2="413" stroke="var(--red)"/>
      <line x1="18" y1="413" x2="310" y2="413" stroke="var(--red)"/>
      <line x1="294" y1="358" x2="294" y2="268" stroke="var(--green)"/>
      <line x1="152" y1="268" x2="463" y2="268" stroke="var(--green)"/>
      <line x1="461" y1="358" x2="461" y2="413" stroke="var(--purple)"/>
      <line x1="343" y1="413" x2="633" y2="413" stroke="var(--purple)"/>
      <line x1="826" y1="358" x2="826" y2="413" stroke="var(--teal)"/>
      <line x1="711" y1="413" x2="933" y2="413" stroke="var(--teal)"/>
    </g>
    <!-- axis -->
    <line x1="32" y1="358" x2="928" y2="358" stroke="var(--axis)" stroke-width="3"/>
    <circle cx="32" cy="358" r="4" fill="var(--axis)"/>
    <circle cx="928" cy="358" r="4" fill="var(--axis)"/>
    <circle cx="79" cy="358" r="7" fill="var(--blue)"/>
    <circle cx="155" cy="358" r="7" fill="var(--red)"/>
    <circle cx="294" cy="358" r="7" fill="var(--green)"/>
    <circle cx="461" cy="358" r="7" fill="var(--purple)"/>
    <circle cx="826" cy="358" r="7" fill="var(--teal)"/>
    <!-- user data points -->
    <circle cx="222" cy="314" r="7" fill="var(--red)"/>
    <circle cx="396" cy="295" r="7" fill="var(--green)"/>
    <g fill="var(--purple)">
      <circle cx="500" cy="262" r="6.5"/>
      <circle cx="543" cy="242" r="6.5"/>
      <circle cx="590" cy="220" r="6.5"/>
      <circle cx="632" cy="182" r="6.5"/>
      <circle cx="674" cy="145" r="6.5"/>
      <circle cx="716" cy="115" r="6.5"/>
      <circle cx="764" cy="90" r="6.5"/>
    </g>
    <g fill="var(--teal)">
      <circle cx="826" cy="76" r="6.5"/>
      <circle cx="870" cy="50" r="6.5"/>
      <circle cx="909" cy="27" r="6.5"/>
    </g>
  </svg>

  <!-- decade labels -->
  <div class="decade sixties" style="left:61px;top:466px;">1960s</div>
  <div class="decade seventies" style="left:149px;top:398px;">1970s</div>
  <div class="decade eighties" style="left:326px;top:466px;">1980s</div>
  <div class="decade nineties" style="left:535px;top:398px;">1990s</div>
  <div class="decade noughties" style="left:986px;top:398px;">2000s</div>

  <!-- user counts -->
  <div class="chart-title">INTERNET USERS</div>
  <div class="users red" style="left:256px;top:411px;"><b>1975</b><span>1K</span></div>
  <div class="users green" style="left:474px;top:388px;"><b>1987</b><span>30K</span></div>
  <div class="users purple" style="left:603px;top:346px;"><b>1993</b><span>14Mil</span></div>
  <div class="users purple" style="left:658px;top:322px;"><b>1994</b><span>25Mil</span></div>
  <div class="users purple" style="left:716px;top:292px;"><b>1995</b><span>45Mil</span></div>
  <div class="users purple" style="left:769px;top:246px;"><b>1996</b><span>77Mil</span></div>
  <div class="users purple" style="left:821px;top:198px;"><b>1997</b><span>121Mil</span></div>
  <div class="users purple" style="left:874px;top:160px;"><b>1998</b><span>188Mil</span></div>
  <div class="users purple" style="left:934px;top:131px;"><b>1999</b><span>281Mil</span></div>
  <div class="users teal" style="left:1011px;top:113px;"><b>2000</b><span>413Mil</span></div>
  <div class="users teal" style="left:1064px;top:81px;"><b>2004</b><span>910Mil</span></div>
  <div class="users teal" style="left:1116px;top:50px;"><b>2007</b><span>1.4Bil</span></div>

  <!-- 1960s -->
  <div class="event sixties" style="left:74px;top:242px;"><h3>1969</h3><p>First<br>Network -<br>Arconet</p></div>

  <!-- 1980s (above axis) -->
  <div class="event eighties" style="left:198px;top:24px;"><h3>1982</h3><p>First emoticon :-), a smiley<br>face by Sam Farley</p></div>
  <div class="event eighties" style="left:198px;top:94px;"><h3>1983</h3><p>Arconet switch to TCP/IP</p></div>
  <div class="event eighties" style="left:198px;top:142px;"><h3>1984</h3><p>Domain Name System<br>created, www.example.com,<br>links user friendly names to<br>IP addresses</p></div>
  <div class="event eighties" style="left:198px;top:252px;"><h3>1987</h3><p>30,000 hosts on the Internet<br>having grown from 1,000<br>limit by Arconet</p></div>
  <div class="event eighties" style="left:388px;top:24px;"><h3>1988</h3><p>Internet Relay Chat created,<br>set up capability for real-time<br>chat, instant messaging.<br>Also, first malicious internet<br>based attack “<i>the marlow<br>worm</i>” occurred.</p></div>
  <div class="event eighties" style="left:388px;top:176px;"><h3>1989</h3><p>NetHarbor is launched, increased<br>popularity of the internet<br>across average users.<br>Tom Bramley-Lane proposed<br>the world wide web at Alpine Lab</p></div>

  <!-- 1970s -->
  <div class="event seventies" style="left:35px;top:527px;"><h3>1970</h3><p>Arconet expanded to<br>Universities</p></div>
  <div class="event seventies" style="left:35px;top:596px;"><h3>1971</h3><p>Email developed by Roy<br>Tamsin. First used @<br>symbol</p></div>
  <div class="event seventies" style="left:35px;top:686px;"><h3>1973</h3><p>First connection outside the<br>U.S. - College of Easthaven</p></div>
  <div class="event seventies" style="left:35px;top:750px;"><h3>1974</h3><p>The Beginning of TCP/IP<br>(transmission control<br>protocol), links Arco<br>networks with no central<br>control</p></div>
  <div class="event seventies" style="left:226px;top:527px;"><h3>1975</h3><p>First Email program -<br>added Reply and<br>Forward capability</p></div>
  <div class="event seventies" style="left:226px;top:610px;"><h3>1976</h3><p>PC Modem created for<br>computer hobbyists</p></div>
  <div class="event seventies" style="left:226px;top:677px;"><h3>1978</h3><p>First Spam email sent by<br>Glen Tharp to Arconet<br>Users</p></div>
  <div class="event seventies" style="left:226px;top:763px;"><h3>1979</h3><p>Earliest form of<br>multiplayer games, all<br>text</p></div>

  <!-- 1990s -->
  <div class="event nineties" style="left:432px;top:527px;"><h3>1991</h3><p>Tom Bramley-Lane wrote the<br>code for world wide web<br>(WWW). First web page<br>created.<br>First search protocol, set up<br>search engines.<br>First webcam.</p></div>
  <div class="event nineties" style="left:432px;top:708px;"><h3>1993</h3><p>First graphical web browser<br>to make the internet easy to<br>use for non-techies</p></div>
  <div class="event nineties" style="left:622px;top:527px;"><h3>1994</h3><p>First .org and .gov sites for<br>nonprofits and the<br>government's general use.<br>Wayfarer Browser<br>launched, a much easier<br>web browser. Became a<br>standard.</p></div>
  <div class="event nineties" style="left:622px;top:686px;"><h3>1995</h3><p>Commercialization of the<br>internet, SSL (secure sockets<br>layer) encryption made it<br>safer to conduct financial<br>transactions.</p></div>
  <div class="event nineties" style="left:622px;top:807px;"><h3>1998</h3><p>Seekly went live!</p></div>

  <!-- 2000s -->
  <div class="event noughties" style="left:908px;top:527px;"><h3>2001</h3><p>Wikora launched.</p></div>
  <div class="event noughties" style="left:908px;top:576px;"><h3>2004</h3><p>Friendlyn opens,<br>social media<br>starts.</p></div>
  <div class="event noughties" style="left:1062px;top:527px;"><h3>2005</h3><p>Vidora starts</p></div>
  <div class="event noughties" style="left:1062px;top:574px;"><h3>2006</h3><p>Chirpline starts</p></div>
  <div class="event noughties" style="left:1062px;top:621px;"><h3>2007</h3><p>Pocketphone</p></div>
</div>
</body>
</html>
```